Brightvale Apparatus Co. Ltd.
Creative Brief
Simple
Obinnaya Kelechukwu
Managing Director
Nigeria: # 42 Adebanwo Close, Kelvale Estate Ashmere, Orivale State USA: PO Box 38192, Larkmoor, TX 70008
+ 234 80 31478265 (Nigeria)
+ 1 555 926 4158 (USA)
+ 1 555 362 8197 (USA)
sales@brightvaleplant.com
www.brightvaleplant.com
Use this address in the letter-head: 58 Kolawale Rd., Ejigbo, Lagos State (Nigeria) 14 Maplerun Dr., Fort Worth, TX 76119 (USA)

```html
<!DOCTYPE html>
<html lang="en">
<head>
<meta charset="utf-8">
<title>Brightvale Apparatus Co. Ltd. — Business Card</title>
<link rel="stylesheet" href="https://fonts.googleapis.com/css2?family=Roboto:ital,wght@0,400;0,700;1,400&display=swap">
<style>
  :root {
    --backdrop: #e9eaec;
    --card: #ffffff;
    --brand-red: #d7151d;
    --ink: #1b1b1b;
    --muted: #666a70;
    --rule: #cfd2d6;
  }
  html, body {
    margin: 0;
    padding: 0;
    width: 1200px;
    height: 874px;
    overflow: hidden;
    background: var(--backdrop);
    font-family: "Roboto", Arial, sans-serif;
  }
  .canvas { position: relative; width: 1200px; height: 874px; }
  .card {
    position: absolute;
    width: 520px;
    height: 297px;
    background: var(--card);
    border-radius: 22px;
    overflow: hidden;
    box-shadow: 0 10px 28px rgba(0,0,0,0.14);
  }
  .card-back { left: 580px; top: 110px; }
  .card-front { left: 100px; top: 440px; }

  .card-back .brand {
    position: absolute;
    inset: 0;
    display: flex;
    align-items: center;
    justify-content: center;
    gap: 16px;
  }
  .brand-dot {
    width: 46px;
    height: 46px;
    border-radius: 50%;
    background: var(--brand-red);
    flex: none;
  }
  .brand-name {
    font-weight: 700;
    color: var(--brand-red);
    font-size: 24px;
    line-height: 1.15;
  }

  .card-front .brand {
    position: absolute;
    left: 28px;
    top: 40px;
    width: 160px;
    display: flex;
    flex-direction: column;
    align-items: flex-start;
    gap: 10px;
  }
  .card-front .brand-dot { width: 38px; height: 38px; }
  .card-front .brand-name { font-size: 15px; }

  .holder {
    position: absolute;
    left: 210px;
    top: 34px;
    right: 24px;
    border-bottom: 1px solid var(--rule);
    padding-bottom: 6px;
  }
  .holder-name {
    margin: 0;
    font-weight: 700;
    font-size: 14px;
    color: var(--brand-red);
  }
  .holder-title {
    margin: 2px 0 0;
    font-style: italic;
    font-size: 10px;
    color: var(--muted);
  }
  .contacts {
    position: absolute;
    left: 210px;
    top: 82px;
    right: 20px;
    margin: 0;
    padding: 0;
    list-style: none;
    font-size: 8.6px;
    line-height: 1.35;
    color: var(--ink);
  }
  .contacts li { display: flex; gap: 7px; margin-bottom: 3px; }
  .contacts svg {
    flex: none;
    width: 10px;
    height: 10px;
    margin-top: 1px;
    fill: var(--muted);
  }
  .swoosh {
    position: absolute;
    left: 0;
    bottom: 0;
    width: 520px;
    height: 297px;
    pointer-events: none;
  }
</style>
</head>
<body>
<main class="canvas">

  <section class="card card-back" aria-label="Business card back">
    <div class="brand">
      <span class="brand-dot"></span>
      <span class="brand-name">Brightvale Apparatus<br>Co. Ltd.</span>
    </div>
  </section>

  <section class="card card-front" aria-label="Business card front">
    <svg class="swoosh" viewBox="0 0 520 297" aria-hidden="true">
      <path d="M0 248 C 170 268, 360 250, 520 196 L520 297 L0 297 Z" fill="var(--brand-red)"/>
      <path d="M0 240 C 170 262, 360 244, 520 186" fill="none" stroke="#ffffff" stroke-width="8"/>
      <path d="M0 226 C 170 250, 350 232, 520 170" fill="none" stroke="var(--ink)" stroke-width="6"/>
    </svg>

    <div class="brand">
      <span class="brand-dot"></span>
      <span class="brand-name">Brightvale Apparatus Co. Ltd.</span>
    </div>

    <header class="holder">
      <p class="holder-name">Obinnaya Kelechukwu</p>
      <p class="holder-title">Managing Director</p>
    </header>

    <ul class="contacts">
      <li>
        <svg viewBox="0 0 10 10"><path d="M5 0a3.5 3.5 0 0 0-3.5 3.5C1.5 6 5 10 5 10s3.5-4 3.5-6.5A3.5 3.5 0 0 0 5 0zm0 5a1.5 1.5 0 1 1 0-3 1.5 1.5 0 0 1 0 3z"/></svg>
        <span># 42 Adebanwo Close, Kelvale Estate<br>Ashmere, Orivale State (Nigeria)</span>
      </li>
      <li>
        <svg viewBox="0 0 10 10"><path d="M5 0a3.5 3.5 0 0 0-3.5 3.5C1.5 6 5 10 5 10s3.5-4 3.5-6.5A3.5 3.5 0 0 0 5 0zm0 5a1.5 1.5 0 1 1 0-3 1.5 1.5 0 0 1 0 3z"/></svg>
        <span>PO Box 38192, Larkmoor, TX 70008 (USA)</span>
      </li>
      <li>
        <svg viewBox="0 0 10 10"><path d="M2 0.5l2 2-1 1.3a6 6 0 0 0 3.2 3.2l1.3-1 2 2-1.2 1.5C4.5 9.5 0.5 5.5 0.5 1.7z"/></svg>
        <span>+ 234 80 31478265 (Nigeria)</span>
      </li>
      <li>
        <svg viewBox="0 0 10 10"><path d="M2 0.5l2 2-1 1.3a6 6 0 0 0 3.2 3.2l1.3-1 2 2-1.2 1.5C4.5 9.5 0.5 5.5 0.5 1.7z"/></svg>
        <span>+ 1 555 926 4158 (USA)</span>
      </li>
      <li>
        <svg viewBox="0 0 10 10"><path d="M2 0.5l2 2-1 1.3a6 6 0 0 0 3.2 3.2l1.3-1 2 2-1.2 1.5C4.5 9.5 0.5 5.5 0.5 1.7z"/></svg>
        <span>+ 1 555 362 8197 (USA)</span>
      </li>
      <li>
        <svg viewBox="0 0 10 10"><path d="M0 2h10v6H0zM0.6 2.4L5 5.6l4.4-3.2v0.9L5 6.6 0.6 3.3z"/></svg>
        <span>sales@brightvaleplant.com</span>
      </li>
      <li>
        <svg viewBox="0 0 10 10"><path d="M5 0a5 5 0 1 0 0 10A5 5 0 0 0 5 0zm0 1c.6.6 1.1 1.8 1.2 3.5H3.8C3.9 2.8 4.4 1.6 5 1zM1 4.5a4 4 0 0 1 1.9-3 6.5 6.5 0 0 0-.6 3zm0 1h1.3c0 1.1.3 2.1.6 3a4 4 0 0 1-1.9-3zM5 9c-.6-.6-1.1-1.8-1.2-3.5h2.4C6.1 7.2 5.6 8.4 5 9zm2.1-.5c.3-.9.6-1.9.6-3H9a4 4 0 0 1-1.9 3zM7.7 4.5c0-1.1-.3-2.1-.6-3A4 4 0 0 1 9 4.5z"/></svg>
        <span>www.brightvaleplant.com</span>
      </li>
    </ul>
  </section>

</main>
</body>
</html>
```